Farhan Jewellers Stationary Contest

Pakistan’s largest Jewellery, Diamond and luxury watches store requires professional stationery. We have a long list of are trusted clients since 1959, our third generation has successfully maintained and sustained the legacy and excellence in the sector.

We require stationery template as part of this contest. The stationery can be double sided.

We prefer a design that makes use of some of the premium business stationery printing options, such as foil stamping, embossing/debossing, painted edges, spot UV etc (doesn't have to use all these options, only what you feel works, but we are looking for a design that stands out and is memorable and these nice touches have that effect.)

We want an eye catching, innovative, high end professional looking stationery for an out of box design that blends well with our new logo (attached). We want the design to be an out of box solution, you may use any element to compliment the logo. You may consider incorporating watermark etc, highlighting our products (Gold and Diamond Jewellery in addition to Luxury watches)

Company details are as follows;

Company name: Farhan Jewellers
Contact Person: Tariq Naveed
Designation: Business Development Consultant
Mobile: +92 333 815 6042
Email: tariqnaveed@mailvora.com
Website: www.farhanjewellers-pk.net

Target Market(s)

Matrimonial, Elite & Businesses class, Upmarket

Font styles to use
Other font styles liked:
• Designers choice

Colors

Designer to choose colors to be used in the design.

Requirements
Must have
• Look and feel: Upmarket, innovative, Modern, Professional, graceful, Elegant, designer stuff.
Nice to have
• Unique design

```html
<!DOCTYPE html>
<html lang="en">
<head>
<meta charset="utf-8">
<title>Farhan Jewellers – Stationery</title>
<link href="https://fonts.googleapis.com/css2?family=Montserrat:wght@500;600&family=Open+Sans:wght@400&display=swap" rel="stylesheet">
<style>
  :root{
    --backdrop:#c9a24f;
    --paper:#f4f4f3;
    --paper-shade:#e6e6e4;
    --gold:#d4a92a;
    --gold-light:#e9c547;
    --gold-deep:#b98d1c;
    --ink:#6b6b6b;
    --watermark:#e3e3e2;
  }
  *{margin:0;padding:0;box-sizing:border-box}
  html,body{width:1200px;height:950px;overflow:hidden}
  body{background:var(--backdrop);position:relative;font-family:"Open Sans",Arial,sans-serif}

  .letterhead,.envelope{position:absolute;width:860px;height:410px;background:var(--paper);box-shadow:0 6px 18px rgba(80,55,10,.25)}
  .letterhead{left:60px;top:45px;overflow:hidden}
  .envelope{left:280px;top:495px;overflow:hidden}

  .letterhead__wedge{position:absolute;left:0;top:0;width:120px;height:410px}

  .brand{position:absolute;display:flex;align-items:center;gap:10px}
  .brand__dot{width:26px;height:26px;border-radius:50%;background:var(--gold)}
  .brand__name{font-family:"Montserrat",Arial,sans-serif;font-weight:600;font-size:22px;letter-spacing:1.5px;color:var(--gold-deep);text-transform:uppercase}

  .letterhead .brand{left:70px;top:70px}
  .letterhead__watermark{position:absolute;left:380px;top:95px;width:170px;height:160px;border-radius:50%;background:radial-gradient(circle,var(--watermark) 0%,var(--paper-shade) 60%,var(--paper) 72%)}

  .contact{position:absolute;left:70px;bottom:34px;list-style:none;font-size:10.5px;line-height:16px;color:var(--ink)}
  .contact li{display:flex;align-items:flex-start;gap:8px}
  .contact svg{width:10px;height:10px;margin-top:3px;flex:none;fill:var(--gold-deep)}

  .envelope__flap{position:absolute;left:0;top:0;width:860px;height:150px}
  .envelope__seam{position:absolute;left:0;top:0;width:860px;height:410px}
  .envelope .brand{right:70px;bottom:90px}
</style>
</head>
<body>

<section class="letterhead" aria-label="Letterhead">
  <svg class="letterhead__wedge" viewBox="0 0 120 410" preserveAspectRatio="none">
    <defs>
      <linearGradient id="wedgeGold" x1="0" y1="0" x2="1" y2="1">
        <stop offset="0" stop-color="var(--gold-light)"/>
        <stop offset="1" stop-color="var(--gold-deep)"/>
      </linearGradient>
    </defs>
    <polygon points="0,0 40,0 0,180" fill="url(#wedgeGold)"/>
  </svg>

  <div class="brand">
    <span class="brand__dot"></span>
    <span class="brand__name">Farhan Jewellers</span>
  </div>

  <div class="letterhead__watermark" role="img" aria-label="Faint embossed ornamental emblem as watermark"></div>

  <ul class="contact">
    <li><svg viewBox="0 0 10 10"><path d="M5 0a3.5 3.5 0 0 0-3.5 3.5C1.5 6 5 10 5 10s3.5-4 3.5-6.5A3.5 3.5 0 0 0 5 0zm0 5a1.5 1.5 0 1 1 0-3 1.5 1.5 0 0 1 0 3z"/></svg><span>14 Gulberg Arcade, Main Boulevard,<br>Lahore, Pakistan</span></li>
    <li><svg viewBox="0 0 10 10"><rect x="2.5" y="0" width="5" height="10" rx="1"/></svg><span>+92 333 815 6042</span></li>
    <li><svg viewBox="0 0 10 10"><path d="M2 0l2 2.5-1 1.2a6 6 0 0 0 3.3 3.3l1.2-1L10 8l-1.5 2C4 10 0 6 0 1.5z"/></svg><span>042-35219480-82</span></li>
    <li><svg viewBox="0 0 10 10"><path d="M0 2h10v6H0zM0 2l5 3.5L10 2" stroke="#f4f4f3" stroke-width=".8"/></svg><span>tariqnaveed@mailvora.com</span></li>
    <li><svg viewBox="0 0 10 10"><circle cx="5" cy="5" r="5"/></svg><span>www.farhanjewellers-pk.net</span></li>
  </ul>
</section>

<section class="envelope" aria-label="Envelope back">
  <svg class="envelope__seam" viewBox="0 0 860 410" preserveAspectRatio="none">
    <path d="M0 410 L60 150 M860 410 L800 150" stroke="var(--paper-shade)" stroke-width="2" fill="none"/>
  </svg>
  <svg class="envelope__flap" viewBox="0 0 860 150" preserveAspectRatio="none" role="img" aria-label="Gold flap lining with geometric pattern">
    <defs>
      <linearGradient id="flapGold" x1="0" y1="0" x2="1" y2="0">
        <stop offset="0" stop-color="var(--gold-deep)"/>
        <stop offset=".5" stop-color="var(--gold-light)"/>
        <stop offset="1" stop-color="var(--gold)"/>
      </linearGradient>
    </defs>
    <path d="M0 0 H860 V60 Q860 80 830 85 L40 150 Q0 150 0 120 Z" fill="url(#flapGold)"/>
  </svg>

  <div class="brand">
    <span class="brand__dot"></span>
    <span class="brand__name">Farhan Jewellers</span>
  </div>
</section>

</body>
</html>
```